Branding Presentation Template for Tavrenholt

I need to build a PowerPoint template that I can use for a brand my company is building out. I don't need a presentation, but I need an actual template I can use to build future presentations.

I already have an AI-generated visual of what I need, but I need help turning this into a template. The final product needs to look just like what I submitted as an attachment or as close to it as possible.

Again, this is for a powerpoint template to be used in future presentations. This is not a presentation itself.

Target Market(s)

Business Owners

Industry/Entity Type

Mechanical Consulting

Font styles to use
Sans Serif

Colors

Designer to choose only greyscale colors for use in the design.

Requirements
Must have
• Powerpoint Template that can be reused for future presenations
Nice to have
• Emailable File Size
Should not have
• A full presentation - this is not a presentation, just a template request.

```html
<!DOCTYPE html>
<html lang="en">
<head>
<meta charset="utf-8">
<title>Tavrenholt — Title Slide Template</title>
<link rel="stylesheet" href="https://fonts.googleapis.com/css2?family=Open+Sans:wght@400;600;700&display=swap">
<style>
  :root {
    --slide-bg: #f4f4f4;
    --ink: #1b1b1b;
    --wordmark: #333333;
    --accent: #f26a1b;
    --muted: #555555;
    --footer-bg: #1a1a1a;
    --footer-ink: #ffffff;
    --texture-deep: #dadada;
    --texture-soft: #e9e9e9;
  }
  * { margin: 0; padding: 0; box-sizing: border-box; }
  html, body {
    width: 1200px; height: 675px; overflow: hidden;
    background: var(--slide-bg);
    font-family: "Open Sans", Arial, sans-serif;
  }
  .slide {
    position: relative; width: 1200px; height: 675px;
    background: var(--slide-bg); overflow: hidden;
  }
  .corner-texture {
    position: absolute; left: 760px; top: 140px; width: 440px; height: 501px;
    background: radial-gradient(ellipse 120% 110% at 100% 100%,
      var(--texture-deep) 0%, var(--texture-soft) 45%, rgba(244,244,244,0) 80%);
  }
  .brand-wordmark {
    position: absolute; left: 56px; top: 84px;
    font-size: 42px; font-weight: 700; letter-spacing: 0.5px;
    color: var(--wordmark); line-height: 1;
  }
  .title-block { position: absolute; left: 56px; top: 235px; }
  .slide-title {
    font-size: 57px; font-weight: 700; color: var(--ink);
    letter-spacing: 0; line-height: 1.1;
  }
  .slide-subhead {
    margin-top: 6px;
    font-size: 28px; font-weight: 400; color: var(--accent);
    letter-spacing: 0.5px; line-height: 1.2;
  }
  .accent-rule {
    position: absolute; left: 56px; top: 368px;
    width: 53px; height: 3px; background: var(--accent);
  }
  .presenter { position: absolute; left: 56px; top: 564px; }
  .presenter-name {
    font-size: 15px; font-weight: 700; letter-spacing: 1px; color: var(--ink);
  }
  .presenter-date {
    margin-top: 2px; font-size: 15px; color: var(--muted); letter-spacing: 0.3px;
  }
  .footer-bar {
    position: absolute; left: 0; top: 641px; width: 1200px; height: 34px;
    background: var(--footer-bg);
    display: flex; align-items: center; justify-content: space-between;
    padding: 0 62px 0 56px;
  }
  .footer-wordmark {
    font-size: 12px; font-weight: 700; color: var(--footer-ink); letter-spacing: 0.3px;
  }
  .page-number { font-size: 11px; color: var(--footer-ink); letter-spacing: 0.5px; }
</style>
</head>
<body>
<main class="slide">
  <div class="corner-texture" role="img" aria-label="Soft grey halftone texture fading into the lower right corner"></div>

  <div class="brand-wordmark">TAVRENHOLT</div>

  <section class="title-block">
    <h1 class="slide-title">PRESENTATION TITLE</h1>
    <p class="slide-subhead">SUBHEAD OR PRESENTATION TOPIC</p>
  </section>

  <div class="accent-rule"></div>

  <section class="presenter">
    <p class="presenter-name">PRESENTER NAME</p>
    <p class="presenter-date">MAY 16, 2026</p>
  </section>

  <footer class="footer-bar">
    <span class="footer-wordmark">TAVRENHOLT</span>
    <span class="page-number">01 / 09</span>
  </footer>
</main>
</body>
</html>
```